Female Focused - Finance Company needs a website

I need a website for a new company based in London called 'Lorinda Pelham Associates'. The company has been set up with a focus on empowering creativity and encouraging women to engage with finance and build their knowledge and understanding. I am targeting professional women and entrepreneurs in the late 20s to 40s age bracket. The mission is to empower women to achieve financial independence and inspire community and connectivity. I want to create a brand that promotes financial security, growth and connectivity.

The website at this stage can be relatively simple, I just want to be able to have a section about me and the work that I do, have contact details for people to be able to get in touch and find out more.

I run a series of different events and want to have a page whereby I can showcase the events that I am running. They can also use links to click through and register for events. I also want to be able to put images up of previous events that I have run. Maybe having a calendar on the website of different things that are happening.

I am creating a membership club called Hop3Hop and I want to have a page whereby they can find out about the membership and the different options that are available.

I have attached the logo below so you can see the designs so far.

I also own the domain name lorindapelhamassociates.com

```html
<!DOCTYPE html>
<html lang="en">
<head>
<meta charset="utf-8">
<title>Lorinda Pelham Associates</title>
<link href="https://fonts.googleapis.com/css2?family=Playfair+Display:wght@400;600&family=Roboto:wght@400;500;700&display=swap" rel="stylesheet">
<style>
:root{
  --plum:#34153d;
  --ink:#3a1a44;
  --orchid:#cf7fd0;
  --violet:#7b6cc4;
  --lav:#8a7fd0;
  --text:#333;
  --muted:#666;
  --soft:#f4f4f4;
  --dark:#2b2b2b;
  --white:#fff;
}
*{margin:0;padding:0;box-sizing:border-box}
html,body{width:1200px;height:4396px;overflow:hidden}
body{position:relative;background:var(--white);font-family:'Roboto',sans-serif;color:var(--text)}
.abs{position:absolute}
.serif{font-family:'Playfair Display',serif}
.brand-mark{position:absolute;border:1px solid #555;border-radius:50%;display:flex;align-items:center;justify-content:center;text-align:center;font-family:'Playfair Display',serif;font-size:9px;line-height:1.2;color:#333;background:var(--white)}
.nav a{position:absolute;top:30px;font-size:11px;font-weight:700;color:#333;text-decoration:none;letter-spacing:.3px}
.btn{position:absolute;display:flex;align-items:center;justify-content:center;background:var(--orchid);color:var(--white);font-size:11px;font-weight:500;border-radius:2px;gap:8px}
.eyebrow{position:absolute;font-size:10px;font-weight:500;letter-spacing:1px;color:#555}
.photo{position:absolute}
.event-card{position:absolute;width:236px;height:230px;background:var(--white);box-shadow:0 2px 10px rgba(0,0,0,.08)}
.event-card .photo{left:0;top:0;width:236px;height:130px}
.event-date{position:absolute;left:12px;top:140px;font-size:10px;font-weight:700;color:var(--lav);display:flex;gap:6px;align-items:center}
.event-title{position:absolute;left:12px;top:162px;width:215px;font-family:'Playfair Display',serif;font-size:12px;line-height:1.6;color:#222}
.dot-btn{position:absolute;width:22px;height:22px;border-radius:50%;background:var(--lav);display:flex;align-items:center;justify-content:center}
.tile{position:absolute;overflow:hidden}
.tile .cap{position:absolute;left:18px;font-family:'Playfair Display',serif;color:var(--white);line-height:1.35}
.tile .meta{position:absolute;left:18px;font-size:10px;color:#b3a9ee}
.tile .go{position:absolute;right:14px}
.blog-card{position:absolute;width:236px;height:230px;background:var(--white);box-shadow:0 2px 10px rgba(0,0,0,.08)}
.blog-card .photo{left:0;top:0;width:236px;height:128px}
.blog-card .pill{position:absolute;right:8px;top:100px;width:22px;height:22px;border-radius:50%;background:var(--lav);display:flex;align-items:center;justify-content:center}
.blog-date{position:absolute;left:15px;top:140px;font-size:10px;font-weight:700;color:var(--lav)}
.blog-text{position:absolute;left:15px;top:160px;width:210px;font-family:'Playfair Display',serif;font-size:12px;line-height:1.6;color:#222}
.quote-mark{position:absolute;font-family:'Playfair Display',serif;font-size:56px;color:var(--orchid);line-height:1}
.quote-text{position:absolute;width:335px;font-size:11.5px;line-height:1.6;color:#666}
.avatar{position:absolute;width:56px;height:56px;border-radius:50%}
.person{position:absolute;font-size:15px;font-weight:500;color:#222}
.role{position:absolute;font-size:9.5px;color:#999}
.role span{color:var(--orchid)}
.field{position:absolute;border:1px solid #ddd;font-size:9px;color:#888;padding:8px 10px;background:var(--white)}
.social{position:absolute;width:22px;height:22px;border-radius:50%;background:var(--lav)}
.foot a{position:absolute;top:4238px;font-size:10.5px;color:#ddd;text-decoration:none}
</style>
</head>
<body>

<!-- Hero backdrop -->
<svg class="abs" style="left:0;top:0" width="1200" height="800" viewBox="0 0 1200 800">
  <rect width="1200" height="360" fill="#f6f6f6"/>
  <path d="M0 230 C200 180 400 320 620 250 C800 190 1000 300 1200 260 L1200 0 L0 0Z" fill="#fafafa"/>
  <path d="M0 655 L0 800 C60 760 120 700 180 655Z" fill="#f3f3f3"/>
</svg>

<!-- Header -->
<div class="brand-mark" style="left:185px;top:25px;width:70px;height:70px">Lorinda<br>Pelham<br>Associates</div>
<nav class="nav">
  <a style="left:488px">HOME</a>
  <a style="left:551px">ABOUT ME</a>
  <a style="left:638px">EVENTS</a>
  <a style="left:711px">NEWS</a>
  <a style="left:773px">MEMBERSHIP</a>
  <a style="left:876px">CONTACT</a>
</nav>
<div class="abs" style="left:488px;top:48px;width:30px;height:2px;background:#333"></div>
<svg class="abs" style="left:946px;top:29px" width="14" height="14" viewBox="0 0 14 14"><circle cx="6" cy="6" r="4.5" fill="none" stroke="#555" stroke-width="1.3"/><line x1="9.5" y1="9.5" x2="13" y2="13" stroke="#555" stroke-width="1.3"/></svg>
<div class="btn" style="left:987px;top:19px;width:100px;height:36px;font-weight:700">Contact Us</div>

<h1 class="abs serif" style="left:0;top:145px;width:1200px;text-align:center;font-weight:400;font-size:40px;line-height:45px;color:var(--ink)">We`re Empowering Creativity &amp;<br>Encouraging to Engage<br>with Finance</h1>
<div class="btn" style="left:587px;top:300px;width:101px;height:36px">Contact us</div>

<div class="photo" role="img" aria-label="Group of smiling women of different ages standing side by side" style="left:0;top:350px;width:1200px;height:305px;background:linear-gradient(90deg,#e9e6e4,#c9a994 20%,#6a5a6e 45%,#8ab8a0 60%,#9b5d6a 80%,#e6dcdc)"></div>

<!-- About -->
<svg class="abs" style="left:143px;top:732px" width="380" height="380" viewBox="0 0 380 380">
  <circle cx="190" cy="190" r="188" fill="none" stroke="#333" stroke-width="2" stroke-dasharray="600 580"/>
</svg>
<div class="photo" role="img" aria-label="Portrait of a smiling woman with glasses in a dark blazer" style="left:163px;top:752px;width:340px;height:340px;border-radius:50%;background:radial-gradient(circle at 50% 40%,#e8d6c2,#c9c9c9 45%,#2f2f35 80%)"></div>

<div class="eyebrow" style="left:558px;top:756px">ABOUT ME</div>
<h2 class="abs serif" style="left:558px;top:780px;width:360px;font-weight:400;font-size:22px;line-height:27px;color:var(--ink)">Feel Confident in you financial<br>future with me</h2>
<div class="abs" style="left:558px;top:847px;width:230px;height:4px;background:linear-gradient(90deg,#555,#fff)"></div>
<p class="abs" style="left:558px;top:872px;width:440px;font-size:11.5px;line-height:19px;font-weight:500;color:#222">Duis ac turpis. Donec sit amet eros. Lorem ipsum dolor sit amet, consectetuer adipiscing elit. Mauris fermentum dictum magna.</p>
<p class="abs" style="left:558px;top:928px;width:440px;font-size:11.5px;line-height:19px;color:#666">Sed laoreet aliquam leo. Ut tellus dolor, dapibus eget, elementum vel, cursus eleifend, elit. Aenean auctor wisi et urna. Aliquam erat volutpat. Duis ac turpis. Integer rutrum ante eu lacus. Vestibulum libero nisl, porta vel, scelerisque eget, malesuada at, neque. Vivamus eget nibh. Etiam cursus leo vel metus.</p>
<div class="btn" style="left:558px;top:1031px;width:101px;height:36px">Contact us</div>

<!-- Events -->
<svg class="abs" style="left:0;top:1100px" width="1200" height="590" viewBox="0 0 1200 590">
  <path d="M0 100 C150 40 300 160 500 110 C700 60 900 150 1200 90 L1200 590 L0 590Z" fill="#f4f4f4"/>
</svg>
<div class="eyebrow" style="left:0;top:1224px;width:1200px;text-align:center">UPCOMING EVENTS</div>
<h2 class="abs serif" style="left:0;top:1247px;width:1200px;text-align:center;font-weight:400;font-size:24px;color:var(--ink)">Attend a Lorinda Pelham Event Today</h2>
<p class="abs" style="left:420px;top:1288px;width:360px;text-align:center;font-size:10.5px;line-height:18px;color:#444">Lorem Ipsum has been the industry's standard dummy text ever since the 1500s, when an unknown printer took a galley of type and scrambled it to make a type specimen book.</p>

<div class="event-card" style="left:239px;top:1366px">
  <div class="photo" role="img" aria-label="Women chatting around a table with laptops" style="background:linear-gradient(135deg,#d8c4a8,#8c6a55 50%,#e8e1d8)"></div>
  <div class="event-date"><svg width="14" height="12"><rect x=".5" y="1.5" width="13" height="10" fill="none" stroke="#8a7fd0"/><line x1="0" y1="4.5" x2="14" y2="4.5" stroke="#8a7fd0"/></svg>JANUARY 24 2023 @ 10:00AM - 12:00PM</div>
  <div class="event-title">Lorem Ipsum is simply dummy text of the printing and typesetting industry</div>
</div>
<div class="event-card" style="left:497px;top:1374px">
  <div class="photo" role="img" aria-label="Woman in a conference audience" style="background:linear-gradient(135deg,#3b5b7d,#1f2d44 60%,#c7a87a)"></div>
  <div class="event-date"><svg width="14" height="12"><rect x=".5" y="1.5" width="13" height="10" fill="none" stroke="#8a7fd0"/><line x1="0" y1="4.5" x2="14" y2="4.5" stroke="#8a7fd0"/></svg>JANUARY 24 2023 @ 10:00AM - 12:00PM</div>
  <div class="event-title">Lorem Ipsum is simply dummy text of the printing and typesetting industry</div>
</div>
<div class="event-card" style="left:754px;top:1374px">
  <div class="photo" role="img" aria-label="Speaker presenting to a large audience" style="background:linear-gradient(135deg,#c9552e,#5a2a22 55%,#e0a070)"></div>
  <div class="event-date"><svg width="14" height="12"><rect x=".5" y="1.5" width="13" height="10" fill="none" stroke="#8a7fd0"/><line x1="0" y1="4.5" x2="14" y2="4.5" stroke="#8a7fd0"/></svg>JANUARY 24 2023 @ 10:00AM - 12:00PM</div>
  <div class="event-title">Lorem Ipsum is simply dummy text of the printing and typesetting industry</div>
</div>
<div class="dot-btn" style="left:594px;top:1629px"><svg width="10" height="8"><path d="M9 4H1M4 1L1 4l3 3" fill="none" stroke="#fff" stroke-width="1.2"/></svg></div>
<div class="dot-btn" style="left:628px;top:1629px"><svg width="10" height="8"><path d="M1 4h8M6 1l3 3-3 3" fill="none" stroke="#fff" stroke-width="1.2"/></svg></div>

<!-- Gallery -->
<div class="eyebrow" style="left:251px;top:1750px">EVENT GALLERY</div>
<h2 class="abs serif" style="left:251px;top:1768px;font-weight:400;font-size:22px;color:var(--ink)">Past Event Showcase</h2>
<div class="btn" style="left:859px;top:1762px;width:143px;height:32px;font-size:10px">More events images <svg width="12" height="8"><path d="M1 4h10M8 1l3 3-3 3" fill="none" stroke="#fff" stroke-width="1.2"/></svg></div>

<div class="tile" style="left:251px;top:1815px;width:480px;height:298px">
  <div class="photo" role="img" aria-label="Woman speaking into a microphone on stage" style="left:0;top:0;width:480px;height:298px;background:radial-gradient(circle at 40% 40%,#4a3f38,#1c1a1c 70%)"></div>
  <div class="cap" style="top:218px;font-size:16px">Lorem Ipsum is simply dummy text of the<br>printing and typesetting industry</div>
  <div class="meta" style="top:268px">Event location | &nbsp;Jan 10 2023</div>
  <svg class="go" style="top:268px" width="14" height="10"><path d="M1 5h12M9 1l4 4-4 4" fill="none" stroke="#fff" stroke-width="1.2"/></svg>
</div>
<div class="tile" style="left:741px;top:1815px;width:261px;height:172px">
  <div class="photo" role="img" aria-label="Presenter facing a seated audience" style="left:0;top:0;width:261px;height:172px;background:linear-gradient(180deg,#d8d4d4,#4a3a3a 70%,#2a2222)"></div>
  <div class="cap" style="top:110px;font-size:11px">Lorem Ipsum is simply dummy text of the<br>printing and typesetting industry</div>
  <div class="meta" style="top:146px;font-size:9px">Event location | &nbsp;Jan 10 2023</div>
  <svg class="go" style="top:147px" width="14" height="10"><path d="M1 5h12M9 1l4 4-4 4" fill="none" stroke="#fff" stroke-width="1.2"/></svg>
</div>
<div class="tile" style="left:741px;top:1997px;width:261px;height:116px">
  <div class="photo" role="img" aria-label="Audience in a dark hall with stage lights" style="left:0;top:0;width:261px;height:116px;background:linear-gradient(135deg,#3a2a5a,#1a1424 60%,#5a3a7a)"></div>
  <div class="cap" style="top:54px;font-size:11px">Lorem Ipsum is simply dummy text of the<br>printing and typesetting industry</div>
  <div class="meta" style="top:90px;font-size:9px">Event location | &nbsp;Jan 10 2023</div>
  <svg class="go" style="top:91px" width="14" height="10"><path d="M1 5h12M9 1l4 4-4 4" fill="none" stroke="#fff" stroke-width="1.2"/></svg>
</div>

<!-- Membership -->
<svg class="abs" style="left:0;top:2176px" width="1200" height="500" viewBox="0 0 1200 500">
  <path d="M0 0H1200V480C1100 470 1000 360 880 410C760 460 640 500 500 430C400 380 380 290 260 300C140 310 60 390 0 440Z" fill="#34153d"/>
  <circle cx="118" cy="384" r="10" fill="#d7cff0"/>
  <circle cx="180" cy="264" r="3" fill="#6a4a74"/>
</svg>
<div class="eyebrow" style="left:251px;top:2221px;color:#ddd">MEMBERSHIP PROGRAM</div>
<h2 class="abs serif" style="left:251px;top:2238px;font-weight:600;font-size:42px;color:var(--white)">Hop3Hop</h2>
<p class="abs" style="left:251px;top:2302px;width:362px;font-size:10.5px;line-height:19px;color:#eee">Lorem Ipsum is simply dummy text of the printing and typesetting industry. Lorem Ipsum has been the industry's standard dummy text ever since the 1500s, when an unknown printer took a galley of type and scrambled it to make a type specimen book. Lorem Ipsum is simply dummy text of the printing and typesetting industry.</p>
<div class="btn" style="left:251px;top:2420px;width:163px;height:31px;font-size:10px">Click here for Membership <svg width="12" height="8"><path d="M1 4h10M8 1l3 3-3 3" fill="none" stroke="#fff" stroke-width="1.2"/></svg></div>
<div class="brand-mark" style="left:759px;top:2259px;width:200px;height:200px;font-size:18px;border:none">Lorinda<br>Pelham<br>Associates</div>

<!-- Blogs -->
<div class="eyebrow" style="left:0;top:2692px;width:1200px;text-align:center">LATEST BLOGS</div>
<h2 class="abs serif" style="left:0;top:2716px;width:1200px;text-align:center;font-weight:400;font-size:23px;color:var(--ink)">Take a look at the latest articles from Lorinda Pelham</h2>

<div class="blog-card" style="left:251px;top:2774px">
  <div class="photo" role="img" aria-label="Conference hall with speaker and screen" style="background:linear-gradient(135deg,#1e2a4a,#3a3a5a 55%,#c08a4a)"></div>
  <div class="pill"><svg width="10" height="8"><path d="M1 4h8M6 1l3 3-3 3" fill="none" stroke="#fff" stroke-width="1.2"/></svg></div>
  <div class="blog-date">JANUARY 24 2023</div>
  <div class="blog-text">Lorem Ipsum is simply dummy text of the printing and typesetting industry. Lorem Ipsum has been the industry's</div>
</div>
<div class="blog-card" style="left:509px;top:2774px">
  <div class="photo" role="img" aria-label="Crowd of women at a networking event" style="background:linear-gradient(135deg,#8a6a3a,#4a3424 55%,#c9a070)"></div>
  <div class="pill"><svg width="10" height="8"><path d="M1 4h8M6 1l3 3-3 3" fill="none" stroke="#fff" stroke-width="1.2"/></svg></div>
  <div class="blog-date">JANUARY 24 2023</div>
  <div class="blog-text">Lorem Ipsum is simply dummy text of the printing and typesetting industry. Lorem Ipsum has been the industry's</div>
</div>
<div class="blog-card" style="left:766px;top:2774px">
  <div class="photo" role="img" aria-label="Women in a workshop discussion" style="background:linear-gradient(135deg,#e8c0c8,#d07a5a 50%,#2a3048)"></div>
  <div class="pill"><svg width="10" height="8"><path d="M1 4h8M6 1l3 3-3 3" fill="none" stroke="#fff" stroke-width="1.2"/></svg></div>
  <div class="blog-date">JANUARY 24 2023</div>
  <div class="blog-text">Lorem Ipsum is simply dummy text of the printing and typesetting industry. Lorem Ipsum has been the industry's</div>
</div>
<div class="dot-btn" style="left:596px;top:3026px"><svg width="10" height="8"><path d="M9 4H1M4 1L1 4l3 3" fill="none" stroke="#fff" stroke-width="1.2"/></svg></div>
<div class="dot-btn" style="left:630px;top:3026px"><svg width="10" height="8"><path d="M1 4h8M6 1l3 3-3 3" fill="none" stroke="#fff" stroke-width="1.2"/></svg></div>
<svg class="abs" style="left:94px;top:2990px" width="14" height="14"><circle cx="7" cy="7" r="7" fill="#e3def5"/></svg>

<!-- Testimonials backdrop -->
<svg class="abs" style="left:0;top:3080px" width="1200" height="500" viewBox="0 0 1200 500">
  <path d="M0 60 C150 140 300 40 500 110 C700 180 900 60 1200 100 L1200 0 L0 0Z" fill="#f4f4f4"/>
  <rect y="480" width="1200" height="20" fill="#f4f4f4"/>
</svg>
<h2 class="abs serif" style="left:0;top:3265px;width:1200px;text-align:center;font-weight:400;font-size:30px;color:var(--ink)">What Our Attendees Are Saying</h2>
<div class="abs" style="left:447px;top:3326px;width:434px;height:5px;background:linear-gradient(90deg,#444,#fff)"></div>

<div class="quote-mark" style="left:232px;top:3362px">"</div>
<p class="quote-text" style="left:289px;top:3382px">Sed laoreet aliquam leo. Ut tellus dolor, dapibus eget, elementum vel, cursus eleifend, elit. Aenean auctor wisi et urna. Aliquam erat volutpat. Duis ac turpis.</p>
<div class="avatar" role="img" aria-label="Headshot of a male attendee" style="left:288px;top:3447px;background:linear-gradient(135deg,#6a8a4a,#b07a5a)"></div>
<div class="person" style="left:358px;top:3459px">Owen Tarrow</div>
<div class="role" style="left:358px;top:3484px">Creative Director at <span>Brightline Studio</span></div>

<div class="quote-mark" style="left:664px;top:3362px">"</div>
<p class="quote-text" style="left:720px;top:3382px">Integer rutrum ante eu lacus. Vestibulum libero nisl, porta vel, scelerisque eget, malesuada at, neque. Vivamus eget nibh. Etiam cursus leo vel metus. Nulla facilisi. Aenean nec eros.</p>
<div class="avatar" role="img" aria-label="Headshot of a female attendee" style="left:721px;top:3447px;background:linear-gradient(135deg,#d8d0cc,#3a2a2a)"></div>
<div class="person" style="left:789px;top:3459px">Mara Lindqvist</div>
<div class="role" style="left:789px;top:3484px">UX/UI designer at <span>Pixel Harbour</span></div>

<svg class="abs" style="left:630px;top:3545px" width="24" height="14"><path d="M23 7H1M7 1L1 7l6 6" fill="none" stroke="#333" stroke-width="1.4"/></svg>
<svg class="abs" style="left:671px;top:3545px" width="24" height="14"><path d="M1 7h22M17 1l6 6-6 6" fill="none" stroke="#8a7fd0" stroke-width="1.4"/></svg>

<!-- Contact -->
<div class="abs" style="left:0;top:3560px;width:1200px;height:500px;background:var(--soft)"></div>
<div class="brand-mark" style="left:280px;top:3679px;width:42px;height:42px;font-size:6px">Lorinda<br>Pelham</div>
<h2 class="abs serif" style="left:280px;top:3738px;font-weight:400;font-size:22px;color:var(--ink)">Contact Me Today</h2>
<p class="abs" style="left:279px;top:3779px;font-size:10px;line-height:15px;color:#333">42 Wren Yard #3, Camden,<br>London NW1 7QP, UK</p>
<p class="abs" style="left:279px;top:3821px;font-size:10px;line-height:14px;color:#333"><span style="color:var(--lav)">QUESTIONS?</span><br>Phone: 020-555-0148<br>Fax: 020-555-0162</p>
<p class="abs" style="left:279px;top:3889px;font-size:10px;color:#333">Email : <span style="color:var(--lav)">info@lorindapelhamassociates.com</span></p>
<div class="social" role="img" aria-label="Social link" style="left:280px;top:3925px"></div>
<div class="social" role="img" aria-label="Social link" style="left:315px;top:3925px"></div>
<div class="social" role="img" aria-label="Social link" style="left:349px;top:3925px"></div>
<div class="social" role="img" aria-label="Social link" style="left:385px;top:3925px"></div>

<div class="abs" style="left:625px;top:3679px;width:401px;height:281px;background:var(--white);box-shadow:0 2px 12px rgba(0,0,0,.08)"></div>
<div class="abs" style="left:625px;top:3706px;width:401px;text-align:center;font-size:11.5px;font-weight:500;color:var(--ink)">Please fill out theform below to contact us</div>
<div class="field" style="left:662px;top:3750px;width:154px;height:29px">Name</div>
<div class="field" style="left:830px;top:3750px;width:155px;height:29px">Email</div>
<div class="field" style="left:662px;top:3795px;width:323px;height:101px">Message</div>
<div class="btn" style="left:763px;top:3909px;width:125px;height:30px;background:var(--violet);font-size:10px;font-weight:700">CONTACT NOW</div>

<!-- Footer -->
<svg class="abs" style="left:0;top:4030px" width="1200" height="366" viewBox="0 0 1200 366">
  <path d="M0 30 C120 80 260 90 420 70 C600 40 780 90 960 60 C1080 40 1150 50 1200 60 L1200 366 L0 366Z" fill="#2b2b2b"/>
</svg>
<div class="brand-mark" style="left:628px;top:4144px;width:60px;height:60px;background:transparent;border-color:#ddd;color:#eee;font-size:8px">Lorinda<br>Pelham<br>Associates</div>
<nav class="foot">
  <a style="left:462px">Home</a>
  <a style="left:524px">About me</a>
  <a style="left:604px">Events</a>
  <a style="left:671px">News</a>
  <a style="left:732px">Membership</a>
  <a style="left:824px">Contact</a>
</nav>
<div class="abs" style="left:300px;top:4276px;width:600px;height:1px;background:#444"></div>
<div class="abs" style="left:0;top:4291px;width:1200px;text-align:center;font-size:8px;color:#ccc">Privacy Policy | Terms of use</div>
<div class="abs" style="left:0;top:4312px;width:1200px;text-align:center;font-size:9px;color:#aaa">Copyright ©2023 lorindapelhamassociates.com</div>

</body>
</html>
```